Velvet Harbour Sessions

Need to improve polish and professionalism of PPT presentation. Get consistent look and feel through whole slides, improved look and feel while maintaining the corporate standards/colour scheme, from the Brimwells corporate presentation. Need everything in Arial font with colours consistent with the PPT template

```html
<!DOCTYPE html>
<html lang="en">
<head>
<meta charset="utf-8">
<title>Velvet Harbour Sessions – Slide Deck</title>
<link href="https://fonts.googleapis.com/css2?family=Arimo:wght@400;700&display=swap" rel="stylesheet">
<style>
:root{
  --red:#c8102e;
  --red-dark:#9e0c23;
  --ink:#2b2d33;
  --charcoal:#33363d;
  --grey:#6d7078;
  --grey-light:#d9dadd;
  --grey-pale:#f1f1f3;
  --green:#3f9b3a;
  --amber:#f2b233;
  --page:#e9eaed;
  --white:#ffffff;
}
*{box-sizing:border-box;margin:0;padding:0}
html,body{width:1200px;height:2736px;overflow:hidden;background:var(--page);font-family:"Arimo",Arial,sans-serif;color:var(--ink)}
.deck{display:grid;grid-template-columns:repeat(3,376px);grid-auto-rows:211px;gap:16px;padding:14px 20px}
.slide{position:relative;background:var(--white);overflow:hidden;box-shadow:0 1px 3px rgba(0,0,0,.18);padding:14px 16px 20px}
.slide.dark{background:var(--charcoal);color:var(--white)}
.s-title{font-size:12px;font-weight:700;line-height:1.2;margin-bottom:3px}
.s-rule{width:26px;height:3px;background:var(--red);margin-bottom:9px}
.s-foot{position:absolute;left:16px;right:16px;bottom:6px;display:flex;justify-content:space-between;align-items:center;font-size:6px;color:var(--grey)}
.s-foot .brand{color:var(--red);font-weight:700;letter-spacing:.08em}
.dark .s-foot{color:#b9bbc0}
.dark .s-foot .brand{color:var(--white)}
.bul{list-style:none;font-size:7px;line-height:1.55;color:var(--ink)}
.bul li{padding-left:8px;position:relative}
.bul li::before{content:"";position:absolute;left:0;top:3px;width:3px;height:3px;background:var(--red)}
.dark .bul{color:var(--white)}
.photo{position:absolute;background:linear-gradient(135deg,#8a7f70,#5b5f66 55%,#3b3e44)}
.photo.warm{background:linear-gradient(160deg,#c9a36b,#8c6f4c 50%,#5a4f45)}
.photo.site{background:linear-gradient(180deg,#9fb0c0,#a08c72 55%,#6a5a4a)}
.row{display:flex;gap:6px;align-items:center}
.box{font-size:7px;font-weight:700;color:var(--white);background:var(--ink);padding:6px 8px;border-radius:3px;text-align:center}
.box.red{background:var(--red)}
.box.grey{background:var(--grey-light);color:var(--ink)}
.op{font-size:11px;font-weight:700;color:var(--red)}
.small{font-size:7px;line-height:1.5}
.lead{font-size:8px;line-height:1.45;color:var(--grey)}
.brandmark{display:flex;align-items:center;gap:5px;font-size:11px;font-weight:700;letter-spacing:.14em;color:var(--white)}
.brandmark i{width:9px;height:9px;background:var(--red);display:block}
.hero-title{font-size:19px;font-weight:700;line-height:1.15;margin-top:30px}
.hero-sub{font-size:10px;margin-top:6px;color:#d8d9dc}
.hero-date{font-size:7px;margin-top:10px;color:#b9bbc0}
.tum{width:100%;border-collapse:collapse;font-size:6.5px}
.tum td{border:1px solid var(--white);padding:3px 4px;text-align:center;color:var(--white);font-weight:700}
.c-grey{background:#8b8e95}.c-green{background:var(--green)}.c-amber{background:var(--amber);color:var(--ink)!important}.c-red{background:var(--red)}.c-ink{background:var(--ink)}
.cal{flex:1;border:1.5px solid var(--red);border-radius:4px;padding:10px 4px;text-align:center;font-size:7px}
.cal b{display:block;font-size:11px;color:var(--red);margin-top:4px}
.tbl{width:100%;border-collapse:collapse;font-size:6.5px}
.tbl th{background:var(--ink);color:var(--white);padding:3px;text-align:left}
.tbl td{padding:3px;border-bottom:1px solid var(--grey-light)}
.tbl tr.hl td{background:#fbe9a6}
.step-panel{position:absolute;left:0;top:0;bottom:0;width:42%;background:var(--charcoal);color:var(--white);padding:16px 14px}
.step-panel .k{font-size:7px;color:#c7c8cc}
.step-panel .n{font-size:22px;font-weight:700;color:var(--red);margin-top:10px}
.step-panel .t{font-size:12px;font-weight:700;line-height:1.2;margin-top:4px}
.step-right{position:absolute;left:46%;right:14px;top:18px}
.flow{display:flex;gap:4px;margin-top:8px}
.flow div{flex:1;background:var(--ink);color:var(--white);font-size:6.5px;font-weight:700;text-align:center;padding:10px 2px;clip-path:polygon(0 0,88% 0,100% 50%,88% 100%,0 100%,12% 50%)}
.flow div.on{background:var(--red)}
.card{background:var(--charcoal);color:var(--white);font-size:7px;line-height:1.45;padding:10px;border-radius:3px}
</style>
</head>
<body>
<main class="deck">

<!-- 1 Title -->
<section class="slide dark">
  <div class="photo" role="img" aria-label="Open-pit mine with haul trucks" style="left:55%;top:0;right:0;bottom:0;opacity:.55"></div>
  <div class="brandmark"><i></i>BRIMWELLS</div>
  <h1 class="hero-title">Velvet Harbour Sessions<br>KPIs &amp; Production Fundamentals</h1>
  <p class="hero-date">November 2023</p>
</section>

<!-- 2 -->
<section class="slide">
  <h2 class="s-title">KPI &amp; Production Fundamentals</h2><div class="s-rule"></div>
  <p class="lead" style="margin-bottom:6px">What we will cover in this session</p>
  <ul class="bul">
    <li>What makes up production</li><li>The Time Usage Model and its categories</li>
    <li>Calendar, available, operating and effective time</li><li>Equipment productivity for haul trucks</li>
    <li>Key measures used on site each shift</li><li>How each KPI links to the mine plan</li>
  </ul>
  <div class="s-foot"><span class="brand">BRIMWELLS</span><span>2</span></div>
</section>

<!-- 3 -->
<section class="slide">
  <div class="photo site" role="img" aria-label="Mine pit and loading equipment" style="left:55%;top:0;right:0;bottom:0"></div>
  <div style="width:50%">
    <h2 class="s-title">KPI &amp; Production Fundamentals</h2><div class="s-rule"></div>
    <ul class="bul"><li>Measure what matters each shift</li><li>Use one shared language for time</li><li>Focus teams on the true constraint</li><li>Review results and act quickly</li></ul>
  </div>
  <div class="s-foot"><span class="brand">BRIMWELLS</span><span>3</span></div>
</section>

<!-- 4 -->
<section class="slide">
  <h2 class="s-title">What Makes up Production</h2><div class="s-rule"></div>
  <p class="lead">In its simplest form, production is a product of rate and time.</p>
  <div class="row" style="margin-top:22px;justify-content:center">
    <div class="box red" style="width:90px">Production</div><span class="op">=</span>
    <div class="box" style="width:80px">Rate</div><span class="op">×</span>
    <div class="box" style="width:80px">Time</div>
  </div>
  <div class="s-foot"><span class="brand">BRIMWELLS</span><span>4</span></div>
</section>

<!-- 5 -->
<section class="slide">
  <h2 class="s-title">What Makes up Production</h2><div class="s-rule"></div>
  <p class="lead">Each element can be broken down further.</p>
  <div class="row" style="margin-top:14px;justify-content:center">
    <div class="box red" style="width:80px">Production</div><span class="op">=</span>
    <div class="box" style="width:80px">Operating Rate</div><span class="op">×</span>
    <div class="box" style="width:80px">Operating Time</div>
  </div>
  <div class="row" style="margin-top:10px;justify-content:flex-end;padding-right:8px">
    <div class="box grey" style="width:80px">Tonnes per hour</div><div class="box grey" style="width:80px">Hours per day</div>
  </div>
  <div class="s-foot"><span class="brand">BRIMWELLS</span><span>5</span></div>
</section>

<!-- 6 -->
<section class="slide">
  <h2 class="s-title">Generic Time Usage Model</h2><div class="s-rule"></div>
  <table class="tum">
    <tr><td colspan="6" class="c-grey">Calendar Time</td></tr>
    <tr><td colspan="5" class="c-ink">Available Time</td><td class="c-red">Downtime</td></tr>
    <tr><td colspan="4" class="c-green">Operating Time</td><td class="c-amber">Standby</td><td class="c-red">Maint.</td></tr>
    <tr><td colspan="3" class="c-green">Effective Time</td><td class="c-amber">Delays</td><td class="c-amber">Idle</td><td class="c-red">Breakdown</td></tr>
  </table>
  <p class="small" style="margin-top:8px;color:var(--grey)">Every hour in the year sits in one category only.</p>
  <div class="s-foot"><span class="brand">BRIMWELLS</span><span>6</span></div>
</section>

<!-- 7 -->
<section class="slide">
  <h2 class="s-title">TUM – Calendar Time</h2><div class="s-rule"></div>
  <p class="lead">Calendar time is all of the time in the period.</p>
  <div class="row" style="margin-top:14px;gap:10px">
    <div class="cal">Calendar time in<br>1 Year<b>8,760 hours</b></div>
    <div class="cal">Calendar time in<br>1 Month<b>720 hours</b></div>
    <div class="cal">Calendar time in<br>1 Day<b>24 hours</b></div>
  </div>
  <div class="s-foot"><span class="brand">BRIMWELLS</span><span>7</span></div>
</section>

<!-- 8 -->
<section class="slide">
  <h2 class="s-title">TUM – Available Time</h2><div class="s-rule"></div>
  <ul class="bul"><li>Time the unit is able to work</li><li>Calendar time less all downtime</li><li>Planned and unplanned maintenance removed</li></ul>
  <table class="tum" style="margin-top:12px">
    <tr><td colspan="6" class="c-grey">Calendar Time</td></tr>
    <tr><td colspan="5" class="c-ink">Available Time</td><td class="c-red">Downtime</td></tr>
  </table>
  <div class="s-foot"><span class="brand">BRIMWELLS</span><span>8</span></div>
</section>

<!-- 9 -->
<section class="slide">
  <h2 class="s-title">TUM – Operating Time</h2><div class="s-rule"></div>
  <ul class="bul"><li>Time the unit is manned and working</li><li>Available time less standby</li><li>Standby covers crib, shift change and no operator</li></ul>
  <table class="tum" style="margin-top:12px">
    <tr><td colspan="5" class="c-ink">Available Time</td><td class="c-red">Down</td></tr>
    <tr><td colspan="3" class="c-green">Operating Time</td><td colspan="2" class="c-amber">Standby</td><td class="c-red">Maint.</td></tr>
  </table>
  <div class="s-foot"><span class="brand">BRIMWELLS</span><span>9</span></div>
</section>

<!-- 10 -->
<section class="slide">
  <h2 class="s-title">TUM – Effective Time</h2><div class="s-rule"></div>
  <ul class="bul"><li>Time the unit is doing productive work</li><li>Operating time less operating delays</li><li>Delays include queuing, waiting and travel</li></ul>
  <table class="tum" style="margin-top:12px">
    <tr><td colspan="4" class="c-green">Operating Time</td><td colspan="2" class="c-amber">Standby</td></tr>
    <tr><td colspan="3" class="c-green">Effective Time</td><td class="c-amber">Delays</td><td colspan="2" class="c-amber">Idle</td></tr>
  </table>
  <div class="s-foot"><span class="brand">BRIMWELLS</span><span>10</span></div>
</section>

<!-- 11 -->
<section class="slide">
  <h2 class="s-title">TUM – Summary</h2><div class="s-rule"></div>
  <table class="tbl">
    <tr><th>Category</th><th>Definition</th><th>KPI</th></tr>
    <tr><td>Calendar</td><td>All hours in period</td><td>100%</td></tr>
    <tr><td>Available</td><td>Calendar less downtime</td><td>Availability</td></tr>
    <tr><td>Operating</td><td>Available less standby</td><td>Utilisation</td></tr>
    <tr><td>Effective</td><td>Operating less delays</td><td>Efficiency</td></tr>
  </table>
  <div class="s-foot"><span class="brand">BRIMWELLS</span><span>11</span></div>
</section>

<!-- 12 -->
<section class="slide">
  <h2 class="s-title">What Makes up Production</h2><div class="s-rule"></div>
  <p class="lead">For a haul truck fleet, the same logic applies.</p>
  <div class="row" style="margin-top:22px;justify-content:center">
    <div class="box red" style="width:90px">Production</div><span class="op">=</span>
    <div class="box" style="width:80px">Payload</div><span class="op">×</span>
    <div class="box" style="width:80px">Cycles</div>
  </div>
  <div class="s-foot"><span class="brand">BRIMWELLS</span><span>12</span></div>
</section>

<!-- 13 -->
<section class="slide">
  <h2 class="s-title">Equipment Productivity – Haul Trucks</h2><div class="s-rule"></div>
  <svg width="344" height="120" viewBox="0 0 344 120">
    <rect x="92" y="6" width="160" height="26" rx="4" fill="#c8102e"/>
    <text x="172" y="23" font-size="9" font-weight="700" fill="#fff" text-anchor="middle" font-family="Arimo,Arial,sans-serif">Equipment Productivity</text>
    <path d="M172 32 V50 M100 50 H244 M100 50 V62 M244 50 V62" stroke="#6d7078" stroke-width="1.2" fill="none"/>
    <rect x="50" y="62" width="100" height="24" rx="12" fill="#2b2d33"/>
    <text x="100" y="77" font-size="8" font-weight="700" fill="#fff" text-anchor="middle" font-family="Arimo,Arial,sans-serif">Payload</text>
    <rect x="194" y="62" width="100" height="24" rx="12" fill="#2b2d33"/>
    <text x="244" y="77" font-size="8" font-weight="700" fill="#fff" text-anchor="middle" font-family="Arimo,Arial,sans-serif">Cycle Time</text>
  </svg>
  <div class="s-foot"><span class="brand">BRIMWELLS</span><span>13</span></div>
</section>

<!-- 14 -->
<section class="slide">
  <h2 class="s-title">Equipment Productivity – Haul Trucks</h2><div class="s-rule"></div>
  <svg width="344" height="130" viewBox="0 0 344 130">
    <line x1="20" y1="115" x2="330" y2="115" stroke="#6d7078"/>
    <path d="M30 114 C110 112 130 20 180 20 C230 20 250 112 325 114 Z" fill="#d9dadd"/>
    <path d="M180 20 C230 20 250 112 325 114 L180 114 Z" fill="#9a9ca2"/>
    <line x1="180" y1="14" x2="180" y2="115" stroke="#c8102e" stroke-width="1.5" stroke-dasharray="3 2"/>
    <path d="M260 60 H200" stroke="#c8102e" stroke-width="6"/>
    <path d="M196 60 l10 -8 v16 z" fill="#c8102e"/>
    <text x="24" y="20" font-size="7" fill="#2b2d33" font-family="Arimo,Arial,sans-serif">Shift the curve left</text>
    <text x="150" y="126" font-size="6" fill="#6d7078" font-family="Arimo,Arial,sans-serif">Payload (t)</text>
  </svg>
  <div class="s-foot"><span class="brand">BRIMWELLS</span><span>14</span></div>
</section>

<!-- 15 -->
<section class="slide">
  <h2 class="s-title">Equipment Productivity – Haul Trucks</h2><div class="s-rule"></div>
  <svg width="344" height="130" viewBox="0 0 344 130">
    <circle cx="172" cy="64" r="46" fill="none" stroke="#d9dadd" stroke-width="2"/>
    <circle cx="172" cy="64" r="22" fill="#c8102e"/>
    <text x="172" y="62" font-size="7" font-weight="700" fill="#fff" text-anchor="middle" font-family="Arimo,Arial,sans-serif">Cycle</text>
    <text x="172" y="71" font-size="7" font-weight="700" fill="#fff" text-anchor="middle" font-family="Arimo,Arial,sans-serif">Time</text>
    <g fill="#2b2d33"><circle cx="172" cy="18" r="10"/><circle cx="218" cy="64" r="10"/><circle cx="172" cy="110" r="10"/><circle cx="126" cy="64" r="10"/><circle cx="205" cy="31" r="8"/><circle cx="139" cy="97" r="8"/></g>
    <g font-size="6.5" fill="#2b2d33" font-family="Arimo,Arial,sans-serif">
      <text x="188" y="14">Load</text><text x="232" y="66">Haul</text><text x="188" y="122">Dump</text><text x="78" y="66">Return</text><text x="216" y="28">Spot</text><text x="100" y="106">Queue</text>
    </g>
  </svg>
  <div class="s-foot"><span class="brand">BRIMWELLS</span><span>15</span></div>
</section>

<!-- 16 Section -->
<section class="slide dark">
  <div class="photo" role="img" aria-label="Mining equipment at dusk" style="left:60%;top:0;right:0;bottom:0;opacity:.4"></div>
  <div class="brandmark"><i></i>BRIMWELLS</div>
  <h1 class="hero-title" style="margin-top:46px">Velvet Harbour Sessions</h1>
  <p class="hero-sub">The Theory of Constraints</p>
</section>

<!-- 17 -->
<section class="slide">
  <h2 class="s-title">Objectives</h2><div class="s-rule"></div>
  <p class="small" style="color:var(--grey)">At the end of this session, you will be able to:</p>
  <svg width="344" height="130" viewBox="0 0 344 130">
    <g transform="translate(172 64)" fill="none" stroke-width="18">
      <circle r="40" stroke="#2b2d33"/>
      <circle r="40" stroke="#c8102e" stroke-dasharray="84 168" transform="rotate(-90)"/>
      <circle r="40" stroke="#9a9ca2" stroke-dasharray="60 192" transform="rotate(30)"/>
    </g>
    <g font-size="6.5" fill="#2b2d33" font-family="Arimo,Arial,sans-serif">
      <text x="10" y="30">Explain the theory</text><text x="10" y="40">of constraints</text>
      <text x="10" y="100">Identify a process</text><text x="10" y="110">bottleneck</text>
      <text x="250" y="30">Apply the five</text><text x="250" y="40">step process</text>
      <text x="250" y="100">Sustain gains</text><text x="250" y="110">over time</text>
    </g>
  </svg>
  <div class="s-foot"><span class="brand">BRIMWELLS</span><span>17</span></div>
</section>

<!-- 18 -->
<section class="slide">
  <h2 class="s-title">Theory of Constraints (ToC)</h2><div class="s-rule"></div>
  <div class="row" style="align-items:flex-start;gap:12px">
    <div class="card" style="width:130px">Every system has at least one constraint that limits its output.</div>
    <ul class="bul" style="flex:1"><li>The constraint sets the pace</li><li>Improving elsewhere adds little</li><li>Focus effort where it counts</li><li>Manage flow to the constraint</li></ul>
  </div>
  <div class="s-foot"><span class="brand">BRIMWELLS</span><span>18</span></div>
</section>

<!-- 19-21 Process bottleneck -->
<section class="slide">
  <h2 class="s-title">Process Bottleneck</h2><div class="s-rule"></div>
  <svg width="344" height="120" viewBox="0 0 344 120">
    <g fill="#3f9b3a"><path d="M14 30 h60 l-18 44 h-24z"/><path d="M100 30 h60 l-18 44 h-24z"/><path d="M272 30 h60 l-18 44 h-24z"/></g>
    <path d="M186 30 h60 l-26 44 h-8z" fill="#c8102e"/>
    <g stroke="#6d7078" stroke-width="1.5"><path d="M78 52 h18"/><path d="M164 52 h18"/><path d="M250 52 h18"/></g>
    <g font-size="6.5" fill="#2b2d33" text-anchor="middle" font-family="Arimo,Arial,sans-serif"><text x="44" y="90">Drill</text><text x="130" y="90">Blast</text><text x="216" y="90">Load</text><text x="302" y="90">Haul</text></g>
  </svg>
  <div class="s-foot"><span class="brand">BRIMWELLS</span><span>19</span></div>
</section>

<section class="slide">
  <h2 class="s-title">Process Bottleneck – Mine Operations</h2><div class="s-rule"></div>
  <svg width="344" height="120" viewBox="0 0 344 120">
    <g fill="#3f9b3a"><path d="M14 30 h60 l-18 44 h-24z"/><path d="M186 30 h60 l-18 44 h-24z"/><path d="M272 30 h60 l-18 44 h-24z"/></g>
    <path d="M100 30 h60 l-26 44 h-8z" fill="#c8102e"/>
    <g stroke="#6d7078" stroke-width="1.5"><path d="M78 52 h18"/><path d="M164 52 h18"/><path d="M250 52 h18"/></g>
    <g font-size="6.5" fill="#2b2d33" text-anchor="middle" font-family="Arimo,Arial,sans-serif"><text x="44" y="90">Drill</text><text x="130" y="90">Load</text><text x="216" y="90">Haul</text><text x="302" y="90">Crush</text></g>
  </svg>
  <div class="s-foot"><span class="brand">BRIMWELLS</span><span>20</span></div>
</section>

<section class="slide">
  <h2 class="s-title">Process Bottleneck – Plant</h2><div class="s-rule"></div>
  <svg width="344" height="120" viewBox="0 0 344 120">
    <g fill="#3f9b3a"><path d="M14 30 h60 l-18 44 h-24z"/><path d="M100 30 h60 l-18 44 h-24z"/><path d="M186 30 h60 l-18 44 h-24z"/></g>
    <path d="M272 30 h60 l-26 44 h-8z" fill="#c8102e"/>
    <g stroke="#6d7078" stroke-width="1.5"><path d="M78 52 h18"/><path d="M164 52 h18"/><path d="M250 52 h18"/></g>
    <g font-size="6.5" fill="#2b2d33" text-anchor="middle" font-family="Arimo,Arial,sans-serif"><text x="44" y="90">Crush</text><text x="130" y="90">Mill</text><text x="216" y="90">Leach</text><text x="302" y="90">Recover</text></g>
  </svg>
  <div class="s-foot"><span class="brand">BRIMWELLS</span><span>21</span></div>
</section>

<!-- 22 -->
<section class="slide">
  <h2 class="s-title">Process Bottleneck – Plant</h2><div class="s-rule"></div>
  <svg width="344" height="120" viewBox="0 0 344 120">
    <g fill="#3f9b3a"><path d="M14 30 h60 l-18 44 h-24z"/><path d="M186 30 h60 l-18 44 h-24z"/><path d="M272 30 h60 l-18 44 h-24z"/></g>
    <path d="M100 30 h60 l-26 44 h-8z" fill="#c8102e"/>
    <g stroke="#6d7078" stroke-width="1.5"><path d="M78 52 h18"/><path d="M164 52 h18"/><path d="M250 52 h18"/></g>
    <text x="172" y="100" font-size="7" fill="#2b2d33" text-anchor="middle" font-family="Arimo,Arial,sans-serif">Mill throughput limits the whole plant</text>
  </svg>
  <div class="s-foot"><span class="brand">BRIMWELLS</span><span>22</span></div>
</section>

<!-- 23 -->
<section class="slide">
  <h2 class="s-title">The Process to Address &amp; Manage Constraints (Bottlenecks)</h2><div class="s-rule"></div>
  <p class="lead">The Theory of Constraints five step process</p>
  <div class="flow" style="margin-top:18px">
    <div class="on">Identify</div><div>Exploit</div><div>Subordinate</div><div>Elevate</div><div>Re-Evaluate</div>
  </div>
  <div class="s-foot"><span class="brand">BRIMWELLS</span><span>23</span></div>
</section>

<!-- 24 -->
<section class="slide">
  <div class="step-panel"><p class="k">The 5 Step Process</p><p class="n">1</p><p class="t">Identify<br>the Process<br>Constraint</p></div>
  <div class="step-right"><p class="small" style="font-weight:700;margin-bottom:6px">Identifying the process constraint</p>
    <ul class="bul"><li>Map the full value chain</li><li>Find where work queues up</li><li>Check rate against plan</li><li>Confirm with site data</li></ul></div>
  <div class="s-foot"><span class="brand">BRIMWELLS</span><span>24</span></div>
</section>

<!-- 25 -->
<section class="slide dark">
  <p class="small" style="color:#c7c8cc">The 5 Step Process</p>
  <p style="font-size:22px;font-weight:700;color:var(--red);margin-top:14px">2</p>
  <p style="font-size:16px;font-weight:700;line-height:1.15;margin-top:2px">Exploit<br>the Process<br>Constraint</p>
  <ul class="bul" style="position:absolute;left:48%;top:40px;right:16px"><li>Never let the constraint stand idle</li><li>Remove waste at the constraint</li><li>Protect it with buffers</li></ul>
  <div class="s-foot"><span class="brand">BRIMWELLS</span><span>25</span></div>
</section>

<!-- 26 -->
<section class="slide dark">
  <p class="small" style="color:#c7c8cc">The 5 Step Process</p>
  <p style="font-size:22px;font-weight:700;color:var(--red);margin-top:14px">3</p>
  <p style="font-size:16px;font-weight:700;line-height:1.15;margin-top:2px">Subordinate<br>Everything<br>Else</p>
  <ul class="bul" style="position:absolute;left:48%;top:40px;right:16px"><li>Align all steps to the constraint</li><li>Pace upstream to its rate</li><li>Avoid excess work in progress</li></ul>
  <div class="s-foot"><span class="brand">BRIMWELLS</span><span>26</span></div>
</section>

<!-- 27 -->
<section class="slide">
  <div class="step-panel"><p class="k">The 5 Step Process</p><p class="n">4</p><p class="t">Elevate<br>the Process<br>Constraint</p></div>
  <div class="step-right"><p class="small" style="font-weight:700;margin-bottom:6px">Elevating the constraint</p>
    <ul class="bul"><li>Add capacity where needed</li><li>Invest only after exploiting</li><li>Review cost against gain</li></ul></div>
  <div class="s-foot"><span class="brand">BRIMWELLS</span><span>27</span></div>
</section>

<!-- 28 -->
<section class="slide">
  <div class="step-panel"><p class="k">The 5 Step Process</p><p class="n">5</p><p class="t">Re-Evaluate<br>the Process</p></div>
  <div class="step-right"><p class="small" style="font-weight:700;margin-bottom:6px">How to identify the next constraint</p>
    <ul class="bul"><li>The constraint may have moved</li><li>Return to step one</li><li>Avoid inertia and old habits</li></ul></div>
  <div class="s-foot"><span class="brand">BRIMWELLS</span><span>28</span></div>
</section>

<!-- 29 -->
<section class="slide">
  <h2 class="s-title">Theory of Constraints &amp; the 5 Step Process</h2><div class="s-rule"></div>
  <table class="tbl">
    <tr><th>Step</th><th>Action</th><th>Owner</th></tr>
    <tr><td>1 Identify</td><td>Find the constraint</td><td>Planning</td></tr>
    <tr class="hl"><td>2 Exploit</td><td>Maximise its output</td><td>Operations</td></tr>
    <tr><td>3 Subordinate</td><td>Align other steps</td><td>Supervisors</td></tr>
    <tr><td>4 Elevate</td><td>Add capacity</td><td>Management</td></tr>
    <tr><td>5 Re-Evaluate</td><td>Repeat the cycle</td><td>All teams</td></tr>
  </table>
  <div class="s-foot"><span class="brand">BRIMWELLS</span><span>29</span></div>
</section>

<!-- 30 Title -->
<section class="slide dark">
  <div class="photo" role="img" aria-label="Gold mine processing site" style="left:55%;top:0;right:0;bottom:0;opacity:.5"></div>
  <div class="brandmark"><i></i>BRIMWELLS</div>
  <h1 class="hero-title" style="font-size:16px">Kestrel Ridge Gold Mine<br>Visual Management &amp;<br>Short Interval Control</h1>
  <p class="hero-date">November 2023</p>
</section>

<!-- 31 -->
<section class="slide">
  <h2 class="s-title">SIC &amp; Visual Management</h2><div class="s-rule"></div>
  <div class="row" style="gap:14px">
    <svg width="120" height="120" viewBox="0 0 120 120">
      <g transform="translate(60 60)" fill="none" stroke-width="22">
        <circle r="40" stroke="#2b2d33"/>
        <circle r="40" stroke="#c8102e" stroke-dasharray="60 192" transform="rotate(-90)"/>
        <circle r="40" stroke="#9a9ca2" stroke-dasharray="60 192" transform="rotate(90)"/>
      </g>
    </svg>
    <ul class="bul" style="flex:1"><li>Plan the shift</li><li>Check progress every interval</li><li>Respond to gaps fast</li><li>Review and learn</li></ul>
  </div>
  <div class="s-foot"><span class="brand">BRIMWELLS</span><span>31</span></div>
</section>

<!-- 32 -->
<section class="slide">
  <div class="photo warm" role="img" aria-label="Mine site with haul road" style="left:0;top:0;width:45%;bottom:0"></div>
  <div style="margin-left:47%">
    <h2 class="s-title">Introduction</h2><div class="s-rule"></div>
    <p class="small" style="font-weight:700">Expectations</p>
    <ul class="bul"><li>Take part and ask questions</li><li>Share site examples</li><li>Apply tools on shift</li></ul>
  </div>
  <div class="s-foot" style="left:47%"><span class="brand">BRIMWELLS</span><span>32</span></div>
</section>

<!-- 33 -->
<section class="slide">
  <div class="photo site" role="img" aria-label="Haul truck on mine bench" style="left:0;top:0;right:0;height:45%"></div>
  <div style="margin-top:88px">
    <h2 class="s-title">Visual Management Process</h2><div class="s-rule"></div>
    <p class="small">Boards show plan against actual so every crew can see the gap.</p>
  </div>
  <div class="s-foot"><span class="brand">BRIMWELLS</span><span>33</span></div>
</section>

<!-- 34 -->
<section class="slide">
  <h2 class="s-title">Visual Management</h2><div class="s-rule"></div>
  <div style="width:52%">
    <ul class="bul"><li>Makes performance visible</li><li>Shows plan against actual</li><li>Flags problems early</li><li>Drives daily conversations</li><li>Owned by the crew</li></ul>
  </div>
  <div class="photo warm" role="img" aria-label="Team reviewing a visual board" style="left:58%;top:14px;right:14px;bottom:22px"></div>
  <div class="s-foot"><span class="brand">BRIMWELLS</span><span>34</span></div>
</section>

<!-- 35 -->
<section class="slide">
  <h2 class="s-title">Visual Management</h2><div class="s-rule"></div>
  <div class="photo" role="img" aria-label="Workers in safety gear at a site board" style="left:16px;top:44px;width:160px;bottom:22px"></div>
  <div class="photo site" role="img" aria-label="Control room screens" style="left:184px;top:44px;right:16px;height:60px"></div>
  <div class="photo warm" role="img" aria-label="Shift meeting on site" style="left:184px;top:110px;right:16px;bottom:22px"></div>
  <div class="s-foot"><span class="brand">BRIMWELLS</span><span>35</span></div>
</section>

</main>
</body>
</html>
```